Harbour Press website re-design

We would like to recreate the www.harbourpress.example.au website into a simpler and more sophisticated version. We want the buyer to be drawn to our site and establish that we are reputable and professional from the moment they enter. We want them to easily find the product or service they are looking for within our site, decide that they would like to find out more and either click through to obtain a quote or click through to contact a rep.

The current website has been created using MS Front Page, however we would like the newly designed site to be created in a mobile responsive WordPress CMS format

We are a Print Broker who can save clients time in hunting around for the right supplier for their print jobs. This is most likely appealing to larger organisations who haven’t got time to waste in finding quotes from many different suppliers for each type of job. We make it easy because we have access to a large network of trade only print & signage suppliers so we can select the best and most cost effective supplier depending on the type of print job. Further, because we don’t do the printing in-house we have low overheads which means we can ensure competitive prices.
Updates

Target Market(s)

Business owners, print managers, receptionists, marketing managers who are time poor, uneducated re:printing, after quick & cost effective solutions

Industry/Entity Type

Printing

Requirements
Must have
• Use the current logo and colours - see files uploaded
Limit scrolling and keep pages within view
Easy to see buttons that navigate the buyer through the site
The site is to be clear, easy to understand, free from clutter (ie.ensure white space) and have a Professional/corporate look
Easy to use Quotation forms
Imagery needs to be modern, and clean -see duskmarble site

Competitor/other websites we like and why?
I like duskmarble.example.au for its’ modern look. I like how the products are displayed in High resolution are very clean and uncluttered. You can easily find the product and access ‘get a quote’.
Calloway Print has a good layout for the quote request. Check out callowayprint.example.au
www.vendrelo.example.au are print brokers/managers. Their descriptions are easy to understand but still heavy in content.
Nice to have
• 1. Home Page
½ page summary of the core business
Distinct buttons for products and services down the side (so that people can go straight to what they need.)
About Us (including profiles); Products and Services; Get a Quote; Contact us across the top

2. About Us
A brief overview of owner, staff and reps. Click through to Profiles for each region rep and contact details either as pop ups or separate pages.

3. Products and Services
Buttons or lists of products link to pop up with get a quote link within (this could be grouped such as Business Cards, Letterheads, Folders etc.; Club printing with plastic cards, sign in books, coasters etc.; Marketing such as flyers, posters, banners etc. (Note. look at how others have broken it up)
Include calling for advice for special products and finishes as service on how a job can be improved and done within budget.
4. Get a Quote
(2 sites mentioned below that I like for the get a quote system)

5. Contact Us
Clear sections divided by lines and details large starting with 1300 number
Head office
Regional numbers and areas they cover
Include emails.

Contact us now or click to request a rep contact you.

```html
<!DOCTYPE html>
<html lang="en">
<head>
<meta charset="utf-8">
<title>Harbour Press – Print Solutions</title>
<link rel="stylesheet" href="https://fonts.googleapis.com/css2?family=Anton&family=Oswald:wght@500&family=Ubuntu:wght@500&family=Yanone+Kaffeesatz:wght@400;600&display=swap">
<style>
:root{
  --brand-red:#c0223f;
  --brand-red-dark:#a51a34;
  --cream:#f3f1ea;
  --footer-bg:#dcd9d3;
  --ring-grey:#b3b3b3;
  --pill-grey:#a9a9a9;
  --text-dark:#333333;
  --heading-grey:#555555;
  --button-grey:#d9d9d9;
  --button-text:#6b6b6b;
}
*{margin:0;padding:0;box-sizing:border-box}
html,body{width:1200px;height:1166px;overflow:hidden}
body{position:relative;background:var(--cream);font-family:Arial,Helvetica,sans-serif;color:var(--text-dark)}
.abs{position:absolute}

/* Hero */
.hero-visual{left:0;top:60px;width:1200px;height:424px;
  background:linear-gradient(110deg,#f2c230 0%,#e9702b 18%,#c93a6a 32%,#5a8fd6 48%,#7cc45a 60%,#f2d64a 72%,#e0452f 86%,#9b3fa4 100%);}
.hero-rule{left:0;top:484px;width:1200px;height:7px;background:#b9b9b9}

/* Header */
.top-strip{left:0;top:0;width:1200px;height:10px;background:#b9b9b9}
.header-band{left:0;top:0;width:1200px;height:115px}
.logo-tab{left:39px;top:0;width:190px;height:156px;background:#fff;border-radius:0 0 26px 26px;
  display:flex;flex-direction:column;align-items:center;justify-content:flex-end;padding-bottom:16px;gap:10px}
.logo-square{width:70px;height:70px;background:var(--brand-red);border-radius:12px}
.logo-name{font-family:"Yanone Kaffeesatz",sans-serif;font-weight:600;font-size:22px;color:var(--brand-red);letter-spacing:.5px}
.main-nav{left:265px;top:24px;display:flex;align-items:center;font-family:"Yanone Kaffeesatz",sans-serif;font-size:27px;color:#fff}
.main-nav a{color:#fff;text-decoration:none}
.main-nav .sep{margin:0 9px}
.phone{left:949px;top:22px;display:flex;align-items:center;gap:16px}
.phone-number{font-family:"Yanone Kaffeesatz",sans-serif;font-size:42px;color:#fff;line-height:1}

/* Hero card */
.promo-card{left:317px;top:113px;width:660px;height:307px;background:#fff;border-radius:12px;text-align:center}
.promo-text{margin:39px auto 0;width:560px;font-family:Ubuntu,sans-serif;font-weight:500;font-size:22px;line-height:29.5px;color:var(--brand-red)}
.inquire-btn{display:inline-block;margin-top:40px;width:329px;height:71px;background:var(--button-grey);border-radius:10px;
  font-family:Anton,sans-serif;font-size:50px;line-height:71px;color:var(--button-text);text-decoration:none;letter-spacing:.5px}
.presenter{border-radius:40px 40px 20px 20px}
.presenter-left{left:228px;top:137px;width:104px;height:285px;background:linear-gradient(180deg,#d9a88a 0%,#c8202c 35%,#a51a24 100%)}
.presenter-right{left:961px;top:184px;width:128px;height:232px;background:linear-gradient(180deg,#8a5533 0%,#e0b596 35%,#2bb7c4 70%,#d9c8bd 100%)}

/* Product circles */
.product{width:232px;text-align:center}
.product-ring{width:232px;height:232px;border-radius:50%;background:#fff;border:7px solid var(--ring-grey);box-shadow:0 2px 4px rgba(0,0,0,.15);overflow:hidden}
.product-photo{width:100%;height:100%;border-radius:50%}
.photo-stickers{background:radial-gradient(circle at 40% 60%,#f2f2f2 0%,#555 60%,#222 100%)}
.photo-banners{background:linear-gradient(135deg,#b8705a 0%,#8a4a3a 45%,#1c1c2a 60%,#d7d7d7 100%)}
.photo-digital{background:linear-gradient(160deg,#5aa7e0 0%,#1f4fa8 50%,#e0462a 80%,#f2d24a 100%)}
.photo-uv{background:linear-gradient(140deg,#2d3236 0%,#8d979c 45%,#3b4246 100%)}
.product-title{margin-top:10px;font-family:"Yanone Kaffeesatz",sans-serif;font-weight:600;font-size:28px;color:var(--brand-red);line-height:1}
.learn-more{display:inline-block;margin-top:8px;width:98px;height:22px;line-height:22px;border-radius:11px;background:var(--pill-grey);
  color:#fff;font-size:12.5px;font-weight:bold;text-decoration:none}

/* Intro */
.intro{left:36px;top:795px;width:600px;font-size:17px;line-height:20.5px;color:var(--text-dark)}
.clients-title{left:38px;top:907px;font-family:Oswald,sans-serif;font-weight:500;font-size:22px;color:#444;letter-spacing:.3px}
.clients-strip{left:36px;top:943px;width:590px;height:68px;background:#fff;border-bottom:3px solid #9a9a9a;box-shadow:0 8px 10px -6px rgba(0,0,0,.35);
  display:flex;align-items:center;justify-content:space-between;padding:0 10px}
.client-list{display:flex;gap:16px;align-items:center;flex:1;justify-content:center}
.client-name{font-family:Arial,Helvetica,sans-serif;font-size:13px;font-weight:bold;color:#555}

/* More products */
.more-title{left:706px;top:790px;font-family:Anton,sans-serif;font-size:33px;color:var(--heading-grey);letter-spacing:.5px}
.product-col{top:845px;list-style:none;font-size:14.5px;line-height:20.8px;color:var(--text-dark)}
.product-col li{display:flex;align-items:center;gap:9px}
.product-col li::before{content:"";width:6px;height:6px;border-radius:50%;border:2.5px solid var(--brand-red);background:#fff;flex:none}
.col-1{left:708px}.col-2{left:893px}.col-3{left:1075px}

/* Footer */
.site-footer{left:0;top:1063px;width:1200px;height:103px;background:var(--footer-bg)}
.footer-nav{left:27px;top:1097px;font-size:15px;color:#444}
.footer-nav a{color:#444;text-decoration:none}
.copyright{left:27px;top:1119px;font-size:12.5px;color:#444}
.footer-mark{left:1103px;top:1092px;width:75px;height:53px;background:#b3aea8;border-radius:9px}
</style>
</head>
<body>

<div class="abs hero-visual" role="img" aria-label="Blurred fan of colourful print swatches"></div>
<div class="abs hero-rule"></div>

<div class="abs top-strip"></div>
<svg class="abs header-band" viewBox="0 0 1200 115" aria-hidden="true">
  <path d="M0 10 H1200 V108 Q760 58 0 80 Z" fill="#d9667c"/>
  <path d="M0 10 H1200 V100 Q760 52 0 74 Z" fill="#c0223f"/>
</svg>

<div class="abs logo-tab">
  <div class="logo-square"></div>
  <div class="logo-name">HARBOUR PRESS</div>
</div>

<nav class="abs main-nav">
  <a href="#">HOME</a><span class="sep">|</span>
  <a href="#">ABOUT</a><span class="sep">|</span>
  <a href="#">PRODUCTS</a><span class="sep">|</span>
  <a href="#">REQUEST A QUOTE</a><span class="sep">|</span>
  <a href="#">CONTACT</a><span class="sep">|</span>
  <a href="#">BLOG</a>
</nav>

<div class="abs phone">
  <svg width="46" height="46" viewBox="0 0 46 46" aria-hidden="true">
    <circle cx="23" cy="23" r="21" fill="none" stroke="#fff" stroke-width="3"/>
    <path d="M17 12 l5 6 -3 3 q2 5 7 8 l3 -3 6 5 -3 4 q-10 0 -17 -10 q-3 -6 0 -10 z" fill="#fff"/>
  </svg>
  <span class="phone-number">1300 555 019</span>
</div>

<div class="abs presenter presenter-left" role="img" aria-label="Man in red shirt holding the sign"></div>
<div class="abs presenter presenter-right" role="img" aria-label="Woman peeking from behind the sign"></div>

<section class="abs promo-card">
  <p class="promo-text">From small run digital, to offset, wide-format, signage, packaging, point of sale or specialist hotel, retail &amp; club supplies our product knowledge is second to none.</p>
  <a class="inquire-btn" href="#">INQUIRE NOW!</a>
</section>

<div class="abs product" style="left:40px;top:446px">
  <div class="product-ring"><div class="product-photo photo-stickers" role="img" aria-label="Car wrapped in printed vinyl stickers"></div></div>
  <div class="product-title">STICKERS</div>
  <a class="learn-more" href="#">learn more</a>
</div>
<div class="abs product" style="left:333px;top:446px">
  <div class="product-ring"><div class="product-photo photo-banners" role="img" aria-label="Vertical street banner on a brick wall"></div></div>
  <div class="product-title">BANNERS</div>
  <a class="learn-more" href="#">learn more</a>
</div>
<div class="abs product" style="left:627px;top:446px">
  <div class="product-ring"><div class="product-photo photo-digital" role="img" aria-label="Wide-format digital printer printing artwork"></div></div>
  <div class="product-title">DIGITAL PRINTING</div>
  <a class="learn-more" href="#">learn more</a>
</div>
<div class="abs product" style="left:925px;top:446px">
  <div class="product-ring"><div class="product-photo photo-uv" role="img" aria-label="Stack of glossy UV coated cards"></div></div>
  <div class="product-title">UV CARDS</div>
  <a class="learn-more" href="#">learn more</a>
</div>

<p class="abs intro">Using Australia's leading print trade suppliers, we provide our clients with the most cost effective print solution in the market.We are constantly sourcing the most advanced technology in the industry to produce the lowest unit price, best quality and fastest Australia wide delivery.</p>

<h2 class="abs clients-title">OUR CLIENTS</h2>
<div class="abs clients-strip">
  <svg width="16" height="28" viewBox="0 0 16 28" aria-hidden="true"><path d="M13 3 L4 14 L13 25" fill="none" stroke="#c0223f" stroke-width="4"/></svg>
  <div class="client-list">
    <span class="client-name">Stride Fitness</span>
    <span class="client-name">Citrus Bowl</span>
    <span class="client-name">Rootstock</span>
    <span class="client-name">Parkvale</span>
    <span class="client-name">Hillside Hire</span>
    <span class="client-name">Ravensgate</span>
  </div>
  <svg width="16" height="28" viewBox="0 0 16 28" aria-hidden="true"><path d="M3 3 L12 14 L3 25" fill="none" stroke="#c0223f" stroke-width="4"/></svg>
</div>

<h2 class="abs more-title">MORE PRODUCTS</h2>
<ul class="abs product-col col-1">
  <li>Beer coasters</li><li>Brochures &amp; flyers</li><li>Carbonless books</li><li>Note pads</li>
  <li>Presentation folders</li><li>School Yearbooks</li><li>Product boxes</li>
</ul>
<ul class="abs product-col col-2">
  <li>Membership cards</li><li>Retail Gift cards</li><li>VIP member cards</li><li>ID cards</li>
  <li>Staff cards</li><li>Access cards</li><li>Student Cards</li><li>Loyalty cards</li>
</ul>
<ul class="abs product-col col-3">
  <li>Posters</li><li>Signage</li><li>Banners</li><li>Stickers</li><li>Wall Sign</li>
</ul>

<footer class="abs site-footer"></footer>
<nav class="abs footer-nav">
  <a href="#">HOME</a> · <a href="#">ABOUT US</a> · <a href="#">PRODUCTS</a> · <a href="#">REQUEST A QUOTE</a> · <a href="#">BLOG</a> · <a href="#">CONTACT</a>
</nav>
<p class="abs copyright">© Copyright Harbour Press - A Division of Coastal Trade Buying Group Pty Limited</p>
<div class="abs footer-mark"></div>

</body>
</html>
```